Business cards for Harbourline Supply Pty Ltd that import building products into Australia from China
Target Market(s)
Business to Business
Industry/Entity Type
Business
Contact Information for Business Card
Front: Logo and Business Name
Rear:
Vernon Asquill
General Manager
Mobile: 0427 196 354
email: vern@harbourlinesupply.com.au
alternative email: vern@ochrefield.com.au
web: www.harbourlinesupply.com.au
Adelaide, Brisbane and Darwin
Colors
ec1f27
fbee3d

```html
<!DOCTYPE html>
<html lang="en">
<head>
<meta charset="utf-8">
<title>Harbourline Supply Pty Ltd – Business Cards</title>
<link rel="stylesheet" href="https://fonts.googleapis.com/css2?family=Lato:wght@400;700;900&display=swap">
<style>
  :root {
    --brand-red: #ec1f27;
    --brand-yellow: #fbee3d;
    --card-dark: #262626;
    --card-mid: #343434;
    --text-light: #f2f2f2;
    --page-bg: #d9d9d9;
  }
  * { box-sizing: border-box; margin: 0; padding: 0; }
  html, body { width: 1200px; height: 900px; overflow: hidden; }
  body {
    background: var(--page-bg);
    font-family: "Lato", Arial, sans-serif;
    position: relative;
  }
  .card {
    position: absolute;
    left: 280px;
    width: 640px;
    height: 366px;
    background: radial-gradient(ellipse at 55% 35%, var(--card-mid), var(--card-dark) 75%);
    box-shadow: 0 10px 28px rgba(0,0,0,0.35);
    overflow: hidden;
    color: var(--text-light);
  }
  .card--front { top: 60px; }
  .card--back { top: 474px; }

  .brand {
    position: absolute;
    display: flex;
    flex-direction: column;
    align-items: center;
    color: var(--brand-yellow);
    font-weight: 900;
    text-transform: uppercase;
  }
  .brand__mark {
    width: 54px; height: 54px;
    border-radius: 50%;
    background: var(--brand-red);
    margin-bottom: 12px;
  }
  .brand__name { font-size: 40px; letter-spacing: 0.5px; line-height: 1; }
  .brand__suffix { font-size: 18px; letter-spacing: 14px; margin-top: 8px; padding-left: 14px; }

  .card--front .brand { left: 0; right: 0; top: 88px; }
  .front__web {
    position: absolute; left: 0; right: 0; top: 270px;
    text-align: center; font-size: 16px; letter-spacing: 1px;
  }

  .card--back .brand { left: 40px; top: 26px; }
  .card--back .brand__mark { width: 40px; height: 40px; margin-bottom: 8px; }
  .card--back .brand__name { font-size: 30px; }
  .card--back .brand__suffix { font-size: 13px; letter-spacing: 11px; margin-top: 6px; }

  .divider {
    position: absolute; left: 30px; top: 150px;
    width: 390px; height: 1.5px; background: var(--brand-red);
  }
  .contacts {
    position: absolute; left: 40px; top: 170px;
    list-style: none; font-size: 15px; line-height: 24px;
  }
  .contacts li { display: flex; align-items: center; gap: 10px; }
  .contacts svg { width: 14px; height: 14px; flex: none; }

  .person {
    position: absolute; right: 36px; top: 124px; text-align: right;
  }
  .person__name { color: var(--brand-red); font-weight: 700; font-size: 25px; }
  .person__role {
    font-size: 17px; padding-bottom: 8px; margin-top: 2px;
    border-bottom: 1.5px solid var(--brand-red); padding-left: 60px;
  }
  .address {
    position: absolute; right: 44px; top: 236px;
    text-align: right; font-size: 18px; line-height: 24px;
  }
  .swoosh { position: absolute; left: 0; top: 0; width: 640px; height: 366px; }
  .back__web {
    position: absolute; left: 250px; bottom: 10px;
    font-size: 17px; color: #fff;
  }
</style>
</head>
<body>

<section class="card card--front">
  <div class="brand">
    <span class="brand__mark"></span>
    <span class="brand__name">Harbourline Supply</span>
    <span class="brand__suffix">Pty Ltd</span>
  </div>
  <p class="front__web">www.harbourlinesupply.com.au</p>
</section>

<section class="card card--back">
  <svg class="swoosh" viewBox="0 0 640 366" aria-hidden="true">
    <path d="M0,258 C120,280 260,308 420,328 C260,304 120,286 0,272 Z" fill="var(--brand-yellow)"/>
    <path d="M0,284 C140,304 300,322 440,326 L640,326 L640,366 L0,366 Z" fill="var(--brand-red)"/>
  </svg>

  <div class="brand">
    <span class="brand__mark"></span>
    <span class="brand__name">Harbourline Supply</span>
    <span class="brand__suffix">Pty Ltd</span>
  </div>

  <span class="divider"></span>

  <ul class="contacts">
    <li>
      <svg viewBox="0 0 14 14"><rect x="3.5" y="0.5" width="7" height="13" rx="1.2" fill="none" stroke="var(--brand-red)" stroke-width="1.4"/><circle cx="7" cy="11" r="0.9" fill="var(--brand-red)"/></svg>
      0427 196 354
    </li>
    <li>
      <svg viewBox="0 0 14 14"><rect x="0.5" y="2.5" width="13" height="9" fill="var(--brand-red)"/><path d="M0.5,2.5 L7,8 L13.5,2.5" fill="none" stroke="var(--card-dark)" stroke-width="1.2"/></svg>
      vern@harbourlinesupply.com.au
    </li>
    <li>
      <svg viewBox="0 0 14 14"><rect x="0.5" y="2.5" width="13" height="9" fill="var(--brand-red)"/><path d="M0.5,2.5 L7,8 L13.5,2.5" fill="none" stroke="var(--card-dark)" stroke-width="1.2"/></svg>
      vern@ochrefield.com.au
    </li>
  </ul>

  <div class="person">
    <p class="person__name">Vernon Asquill</p>
    <p class="person__role">General Manager</p>
  </div>

  <p class="address">14 Wharf Street<br>Darwin NT 0800</p>

  <p class="back__web">www.harbourlinesupply.com.au</p>
</section>

</body>
</html>
```